Boat Hire Website - Building on the existing web design

Keel Charter Co connects boat owners with people looking to charter a boat for their next big event.
There are now over 30 boats to choose from, so I need a nifty filter system to instantly reduce 30 boats down to a small number, based on some user preferences.
I want to use Ajax or similar so that the collection of boats instantly changes in front of you, rather than reloading.

Here is the page we are working with:
http://www.keelcharterco.com.au/c/all_boats

The page should not look drastically different to every other page on the site, so I suggest keeping the entire header section and the blue background but I'm open to ideas.
Your goal is to add dials / gauges / filters / input boxes or whetever way you can think of to allow the user to filter the list of suitable boats for them.
The attributes they can adjust are:
1. Number of guests (overall max is 400)
2. Budget (not exact figures, more like Luxury, Mid-High Range, Mid Range, Budget).

I suggest changing the profile images to make them very small so you can see them all on one page.
It's optional whether you keep all the other info on each boat, such as the short description, the attributes such as BBQ, the enquiry forms.
You must keep the Boat hire cost and the suitable for x number of guests part in some way for each boat.

Things we like:
Smooth, cool designs
Very easy to understand and use

Things we don't want:
Pagination
Updates

Hey All,

Just to let you know, I've now guaranteed payment.

Thanks to the 2 designers for their work so far.

Marv.

Thanks for all the designs to date, we're getting closer but still not quite there yet.

Here's a summary of what's been working well so far:
1. Leave the header of the page untouched (http://www.keelcharterco.com.au/c/all_boats) from the logo down to the water line.
2. I like 2 horizontal sliders below the water line for filtering on number of guests and Quality/Budget. Ideally not taking too much vertical space.
3. I like small tiled boat images representing each boat, with at least 3 in each row. 
I like designs where hovering over the individual boat images blacks it out and reveals more info such as price, number of guests, short description, Enquire and (More Info) buttons. Unfortunately I don't think there's enough space to show the attributes such as BBQ?
The more boat images I can see above the fold the better, but unfortunately the smaller they are, the less room there is for extra info to be displayed when hovering over them.

Thanks and I look forward to more designs in the next couple of days.

Target Market(s)

Age 21 - 50

Industry/Entity Type

Building

```html
<!DOCTYPE html>
<html lang="en">
<head>
<meta charset="utf-8">
<title>All Boats – Keel Charter Co</title>
<link href="https://fonts.googleapis.com/css2?family=Roboto:wght@400;500;700&display=swap" rel="stylesheet">
<style>
:root{
  --sky-top:#3d93d6;
  --sky-mid:#7fc0ec;
  --water:#1f93d0;
  --water-deep:#1a8bc8;
  --navy:#17507f;
  --nav-top:#3c9ad4;
  --nav-bottom:#1d7bba;
  --orange:#f46a0c;
  --orange-light:#ff8a22;
  --gold:#ffb400;
  --panel:rgba(255,255,255,0.88);
  --panel-soft:rgba(235,247,253,0.9);
  --text:#555f66;
  --text-dark:#2f3a40;
  --white:#ffffff;
  --cyan:#2bb0ea;
  --tile-band:rgba(20,24,28,0.82);
  --link:#164c7c;
}
*{box-sizing:border-box;margin:0;padding:0}
html,body{width:973px;height:1200px;overflow:hidden}
body{
  font-family:'Roboto',Arial,sans-serif;
  position:relative;
  background:
    linear-gradient(180deg,var(--sky-top) 0px,var(--sky-mid) 200px,#cfeaf8 320px,#e6f5fc 336px,#5eb6e3 342px,var(--water) 460px,var(--water-deep) 1200px);
  color:var(--text);
}
.abs{position:absolute}

/* Brand */
.brand{left:0;width:973px;top:60px;text-align:center}
.brand-mark{display:inline-flex;align-items:center;gap:10px}
.brand-dot{width:34px;height:34px;border-radius:50%;background:var(--white)}
.brand-name{font-size:30px;font-weight:700;color:var(--navy);letter-spacing:0.5px}

/* Navigation */
.main-nav{left:97px;top:174px;width:779px;height:41px;
  background:linear-gradient(180deg,var(--nav-top),var(--nav-bottom));
  display:flex;align-items:center;padding-left:56px}
.main-nav a{color:#e8f4fc;font-size:12.5px;font-weight:500;text-decoration:none;margin-right:40px}
.main-nav a.current{color:var(--white);font-weight:700}
.nav-sep{width:1px;height:27px;background:rgba(255,255,255,0.35);margin-right:30px;margin-left:-12px}

/* Find panel */
.find-panel{left:97px;top:231px;width:779px;height:97px;background:var(--panel)}
.find-title{left:9px;top:16px;font-size:20px;color:var(--orange);font-weight:500}
.help-title{left:317px;top:17px;font-size:12.5px;color:var(--navy);font-weight:500}
.panel-rule{left:0;top:36px;width:779px;height:1px;background:#d6dde2}
.field{height:27px;background:var(--white);border:1px solid #d3d8dc;font-size:10px;color:#666;padding:8px 8px;box-shadow:inset 0 1px 2px rgba(0,0,0,0.06)}
.btn-orange{height:27px;background:linear-gradient(180deg,var(--orange-light),var(--orange));color:var(--white);font-size:10px;font-weight:700;display:flex;align-items:center;justify-content:center;border:1px solid #e05a00}
.caret{position:absolute;right:10px;top:11px;width:0;height:0;border-left:4px solid transparent;border-right:4px solid transparent;border-top:6px solid #aaa}

/* Filter panel */
.filter-panel{left:97px;top:343px;width:779px;height:146px;background:var(--panel-soft)}
.filter-label{font-size:11px;color:var(--text)}
.slider{width:420px;height:22px;border-radius:11px;background:linear-gradient(180deg,#fff,#ececec);border:1px solid #d0d6da}
.slider-track{position:absolute;left:9px;right:9px;top:7px;height:6px;border-radius:3px;background:#dcdfe1;box-shadow:inset 0 1px 1px rgba(0,0,0,0.15)}
.slider-fill{position:absolute;top:0;height:6px;background:linear-gradient(180deg,#7dc7f2,#3f9ee0);border-radius:3px}
.slider-thumb{position:absolute;top:-4px;width:12px;height:14px;border-radius:3px;background:linear-gradient(180deg,#fff,#d8d8d8);border:1px solid #a8a8a8}
.scale{width:420px;display:flex;justify-content:space-between;font-size:7.5px;font-weight:700;color:#556;padding:0 0 0 11px}
.check{display:flex;align-items:center;gap:6px;font-size:9.5px;color:var(--text)}
.box{width:11px;height:11px;background:var(--white);border:1px solid #cdd3d7}

/* Boats */
.section-title{font-size:15px;color:var(--navy);font-weight:500}
.pager{left:821px;top:502px;width:55px;height:27px;background:var(--white);display:flex}
.pager span{flex:1;display:flex;align-items:center;justify-content:center;border-right:1px solid #e2e2e2}
.boats-panel{left:97px;top:536px;width:779px;height:389px;background:rgba(255,255,255,0.85)}
.tile{width:179px;height:179px;overflow:hidden}
.tile-photo{position:absolute;inset:0}
.tile-band{position:absolute;left:0;right:0;bottom:0;height:32px;background:var(--tile-band);color:var(--cyan);font-size:12px;font-weight:500;padding:10px 4px;text-transform:uppercase}
.tile-detail{background:#1b1e22;color:var(--white);padding:18px 4px 0 4px}
.tile-detail h3{font-size:15px;font-weight:400;color:var(--cyan);margin-bottom:5px}
.tile-detail p{font-size:9px;line-height:12px;text-align:justify}
.tile-detail .meta{color:var(--cyan);font-size:10px;line-height:13px;margin-top:8px}
.tile-actions{display:flex;gap:6px;margin-top:7px}
.tile-actions span{height:25px;display:flex;align-items:center;justify-content:center;font-size:10px;color:var(--white)}
.quote{width:82px;background:linear-gradient(180deg,#38b9ef,#1d93d0)}
.more{width:82px;background:linear-gradient(180deg,var(--orange-light),var(--orange))}

/* Useful info */
.info-title{left:0;width:973px;top:935px;text-align:center;font-size:15px;color:#e8f6fd}
.info-card{width:240px}
.info-card h4{font-size:11.5px;font-weight:400;color:var(--gold);line-height:14px;margin-bottom:2px}
.info-card p{font-size:10px;line-height:15px;color:#e6f4fb}
.footer-rule{left:97px;top:1048px;width:779px;height:1px;background:rgba(255,255,255,0.25)}

/* Footer */
.foot-brand{left:97px;top:1090px;display:flex;align-items:center;gap:6px}
.foot-brand .brand-dot{width:18px;height:18px}
.foot-brand span{font-size:14px;font-weight:700;color:var(--navy)}
.foot-col h5{font-size:12px;font-weight:500;color:var(--white);margin-bottom:8px}
.foot-col a{display:block;font-size:10.5px;color:var(--link);text-decoration:underline;line-height:18.5px}
.social{display:flex;align-items:center;gap:5px;width:70px;height:21px;background:var(--white);border:1px solid #c7ccd2;padding:0 4px;font-size:7px;color:#3a4f7a;line-height:8px}
.social i{width:11px;height:11px;background:#3b5a99;display:block}
.copyright{left:0;width:973px;top:1163px;text-align:center;font-size:9px;color:var(--link)}
</style>
</head>
<body>

<header>
  <div class="abs brand">
    <div class="brand-mark"><span class="brand-dot"></span><span class="brand-name">Keel Charter Co</span></div>
  </div>
  <nav class="abs main-nav">
    <a href="#">Home</a><a href="#">Parties</a><a href="#">Weddings</a><a href="#">Corporate events</a><a href="#" class="current">All Boats</a><span class="nav-sep"></span><a href="#">Useful info</a><a href="#">My Charter</a>
  </nav>
</header>

<section class="abs find-panel">
  <div class="abs find-title">FIND A BOAT</div>
  <div class="abs help-title">GET HELP FROM KEEL CHARTER CO - 0400 555 018</div>
  <div class="abs panel-rule"></div>
  <div class="abs field" style="left:9px;top:48px;width:217px">All Boats<span class="caret"></span></div>
  <div class="abs btn-orange" style="left:234px;top:48px;width:60px">SEARCH</div>
  <div class="abs field" style="left:318px;top:48px;width:192px">How can we help?</div>
  <div class="abs field" style="left:522px;top:48px;width:160px">Enter your Email Address</div>
  <div class="abs btn-orange" style="left:694px;top:48px;width:77px">GET ENQUIRY!</div>
</section>

<section class="abs filter-panel">
  <div class="abs filter-label" style="left:9px;top:9px">Approx Number of Guests</div>
  <div class="abs slider" style="left:9px;top:32px">
    <div class="slider-track"><div class="slider-fill" style="left:30px;width:88px"></div>
      <div class="slider-thumb" style="left:24px"></div><div class="slider-thumb" style="left:112px"></div></div>
  </div>
  <div class="abs scale" style="left:9px;top:57px"><span>0</span><span>100</span><span>200</span><span>300</span><span>400</span><span>MAX</span></div>

  <div class="abs filter-label" style="left:10px;top:77px">Boat Quality</div>
  <div class="abs slider" style="left:9px;top:98px">
    <div class="slider-track"><div class="slider-fill" style="left:30px;width:88px"></div>
      <div class="slider-thumb" style="left:24px"></div><div class="slider-thumb" style="left:112px"></div></div>
  </div>
  <div class="abs scale" style="left:9px;top:123px"><span>Normal</span><span>Budge</span><span>Mid-Range</span><span>Luxury</span><span>5 Star</span><span>MAX</span></div>

  <div class="abs filter-label" style="left:470px;top:9px">Specific Requirements</div>
  <div class="abs check" style="left:470px;top:44px"><svg class="box" viewBox="0 0 11 11"><path d="M2.5 5.5l2 2 4-5" fill="none" stroke="#1d5f9a" stroke-width="1.5"/></svg>All Boats</div>
  <div class="abs check" style="left:599px;top:44px"><svg class="box" viewBox="0 0 11 11"><path d="M2.5 5.5l2 2 4-5" fill="none" stroke="#1d5f9a" stroke-width="1.5"/></svg>All Boats</div>
  <div class="abs check" style="left:470px;top:78px"><span class="box"></span>Christmas Parties</div>
  <div class="abs check" style="left:599px;top:78px"><span class="box"></span>Christmas Parties</div>
  <div class="abs check" style="left:470px;top:112px"><span class="box"></span>Corporate Cruises</div>
  <div class="abs check" style="left:599px;top:112px"><span class="box"></span>Corporate Cruises</div>
</section>

<h2 class="abs section-title" style="left:96px;top:507px">ALL BOATS</h2>
<div class="abs pager">
  <span><svg width="8" height="10" viewBox="0 0 8 10"><path d="M6 1L2 5l4 4" fill="none" stroke="#bbb" stroke-width="1.2"/></svg></span>
  <span style="border:none"><svg width="8" height="10" viewBox="0 0 8 10"><path d="M2 1l4 4-4 4" fill="none" stroke="#bbb" stroke-width="1.2"/></svg></span>
</div>

<section class="abs boats-panel">
  <article class="abs tile tile-detail" style="left:8px;top:10px">
    <h3>Harbourlight</h3>
    <p>This is the perfect vessel for corporate entertaining, built to offer superlative luxury for the discerning guest.</p>
    <div class="meta">Suits: 1-49 Guests</div>
    <div class="meta">Boat hire only cost:<br>$3,400 - $4,400 / 4 hours</div>
    <div class="tile-actions"><span class="quote">GET A QUOTE</span><span class="more">MORE INFO</span></div>
  </article>

  <article class="abs tile" style="left:203px;top:10px">
    <div class="tile-photo" role="img" aria-label="Sailing yacht heeling on open water" style="background:linear-gradient(160deg,#c9d6dd,#5f7f8c 50%,#1f4a5c)"></div>
    <div class="tile-band">Seabreeze 40</div>
  </article>
  <article class="abs tile" style="left:398px;top:10px">
    <div class="tile-photo" role="img" aria-label="Deck winches on a white catamaran under blue sky" style="background:linear-gradient(170deg,#6fa4d4,#c7d2da 45%,#6d7378)"></div>
    <div class="tile-band">Marlowe</div>
  </article>
  <article class="abs tile" style="left:592px;top:10px">
    <div class="tile-photo" role="img" aria-label="Deck winches on a white catamaran under blue sky" style="background:linear-gradient(170deg,#6fa4d4,#c7d2da 45%,#6d7378)"></div>
    <div class="tile-band">Marlowe</div>
  </article>

  <article class="abs tile" style="left:8px;top:200px">
    <div class="tile-photo" role="img" aria-label="Large white cruiser on the harbour with city skyline" style="background:linear-gradient(180deg,#8ec0e8,#c8ccc8 45%,#e8ecee 75%,#53728a)"></div>
    <div class="tile-band">Bayview</div>
  </article>
  <article class="abs tile" style="left:203px;top:200px">
    <div class="tile-photo" role="img" aria-label="Speedboat cutting through spray" style="background:linear-gradient(170deg,#3c6f8c,#b9c8d0 50%,#2f5f78)"></div>
    <div class="tile-band">Swiftline</div>
  </article>
  <article class="abs tile" style="left:398px;top:200px">
    <div class="tile-photo" role="img" aria-label="White motor cruiser on calm water" style="background:linear-gradient(180deg,#6d9cc9,#cfd6da 55%,#355d7c)"></div>
    <div class="tile-band">Seabreeze 40</div>
  </article>
  <article class="abs tile" style="left:591px;top:200px">
    <div class="tile-photo" role="img" aria-label="White motor cruiser on calm water" style="background:linear-gradient(180deg,#6d9cc9,#cfd6da 55%,#355d7c)"></div>
    <div class="tile-band">Seabreeze 40</div>
  </article>
</section>

<section>
  <h2 class="abs info-title" style="font-weight:400">USEFUL INFO</h2>
  <div class="abs info-card" style="left:105px;top:971px">
    <h4>TOP 3 THINGS TO DO IN SYDNEY</h4>
    <p>Sydney lies in one of the world's most beautiful harbours, Sydney Harbour, here we list th...</p>
  </div>
  <div class="abs info-card" style="left:365px;top:971px">
    <h4>Treat Yourself with a Pamper Cruise<br>on Sydney Harbour</h4>
    <p>Sydney lies in one of the world's most beautiful harbours, Sydney Harbour, here we list th...</p>
  </div>
  <div class="abs info-card" style="left:625px;top:971px">
    <h4>TOP 3 THINGS TO DO IN SYDNEY</h4>
    <p>Sydney lies in one of the world's most beautiful harbours, Sydney Harbour, here we list th...</p>
  </div>
</section>

<div class="abs footer-rule"></div>

<footer>
  <div class="abs foot-brand"><span class="brand-dot"></span><span>Keel Charter Co</span></div>
  <div class="abs foot-col" style="left:222px;top:1065px"><h5>Find a boat</h5><a href="#">Parties</a><a href="#">Weddings</a><a href="#">Corporate events</a></div>
  <div class="abs foot-col" style="left:364px;top:1065px"><h5>Keel Charter Co</h5><a href="#">Contact us</a><a href="#">About us</a><a href="#">Site map</a></div>
  <div class="abs foot-col" style="left:496px;top:1065px"><h5>Community</h5><div class="social"><i></i><span>Find us on<br>Harbour Social</span></div></div>
  <div class="abs foot-col" style="left:650px;top:1065px"><h5>General</h5><a href="#">FAQ</a><a href="#">Terms &amp; conditions</a><a href="#">Privacy policy</a></div>
  <div class="abs foot-col" style="left:781px;top:1065px"><h5>Boat owners</h5><a href="#">Add your boat</a><a href="#">Client login</a></div>
  <div class="abs copyright">© Copyright 2010 Keel Charter Co</div>
</footer>

</body>
</html>
```